Business cards and stationary design

We just completed the design of our new logo and we need to print new business cards and letterhead for our nonprofit. We are looking for a fresh new design that shows off our new logo. On letterhead, we must have a column on the right or left to include our Board of Directors (up to 45 names) (see attachment)

Industry/Entity Type

Non-Profit

Contact Information for Business Card

Standard business card with name, title, Company name, mailing address phone numbers, email address and website. Tagline on back "Bringing the homeless home"

Font styles to use
Sans Serif

Requirements
Must have
• include pertinent information above
• new logo
• fonts compatible with logo
• should use logo colors only
Nice to have
• tag lines

```html
<!DOCTYPE html>
<html lang="en">
<head>
<meta charset="utf-8">
<title>Harbor Shelter Alliance – Letterhead</title>
<link href="https://fonts.googleapis.com/css2?family=Questrial&family=Roboto:wght@400;500&display=swap" rel="stylesheet">
<style>
  :root{
    --backdrop:#e3e3e3;
    --paper:#f1f1f1;
    --paper-edge:#e7e7e7;
    --ink:#555555;
    --ink-strong:#3d3d3d;
    --brand-blue:#1f7fb0;
    --brand-red:#d62e2e;
    --signature:#2f6db5;
  }
  html,body{margin:0;padding:0;width:1024px;height:1200px;overflow:hidden;background:var(--backdrop);}
  .letterhead{
    position:absolute;left:97px;top:20px;width:829px;height:1160px;
    background:linear-gradient(90deg,var(--paper) 0%,var(--paper-edge) 100%);
    box-shadow:0 2px 8px rgba(0,0,0,.12);
    color:var(--ink);
  }
  .brand{position:absolute;left:82px;top:132px;width:230px;display:flex;align-items:center;gap:10px;}
  .brand-mark{flex:none;width:14px;height:14px;border-radius:50%;background:var(--brand-red);}
  .brand-name{font-family:'Questrial',sans-serif;font-size:18px;letter-spacing:1.5px;color:var(--brand-blue);line-height:21px;}
  .sender{position:absolute;left:352px;top:80px;font-family:'Roboto',sans-serif;font-size:12px;line-height:14px;color:var(--ink);font-style:normal;}
  .sender p{margin:0 0 6px;}
  .board{position:absolute;left:615px;top:76px;font-family:'Roboto',sans-serif;font-size:12.3px;color:var(--ink);}
  .board-title{margin:0 0 34px;font-weight:500;color:var(--ink-strong);font-size:12.3px;}
  .officers,.members{list-style:none;margin:0;padding:0;}
  .officers li{height:23.65px;}
  .officers strong{font-weight:500;color:var(--ink-strong);}
  .members{margin-top:21px;}
  .members li{height:23.65px;}
  .letter{position:absolute;left:85px;top:276px;width:439px;font-family:'Questrial',sans-serif;}
  .salutation{font-size:21px;margin:0 0 42px;color:var(--ink);font-weight:400;}
  .letter-body p{font-size:13px;line-height:17.8px;text-align:justify;hyphens:auto;-webkit-hyphens:auto;margin:0 0 17.8px;color:var(--ink);}
  .closing{position:absolute;left:85px;top:870px;font-family:'Questrial',sans-serif;font-size:12.6px;margin:0;}
  .signature{position:absolute;left:81px;top:893px;width:124px;height:56px;}
</style>
</head>
<body>
<main class="letterhead">
  <header>
    <div class="brand">
      <span class="brand-mark"></span>
      <span class="brand-name">HARBOR SHELTER<br>ALLIANCE</span>
    </div>
    <address class="sender">
      <p>HARBOR SHELTER ALLIANCE<br>4210 Birchwood Way<br>Fairview, Alaska 99512</p>
      <p>555 218 0147<br>owen@harborshelteralliance.org<br>www.harborshelteralliance.org</p>
    </address>
  </header>

  <aside class="board">
    <h2 class="board-title">Board of Directors:</h2>
    <ul class="officers">
      <li><strong>Elliot Barrow</strong>,Chair</li>
      <li><strong>Grant Pullman</strong>,Vice Chair</li>
      <li><strong>Rita Ashford</strong>,Treasurer</li>
      <li><strong>Anna Alder</strong>, Secretary</li>
    </ul>
    <ul class="members">
      <li>Kevin Abbot</li><li>Joel Baines</li><li>Tim Bradfield</li><li>Ella Bristow</li>
      <li>Bill Burrows</li><li>Alan Chester</li><li>Brenda Colley</li><li>Karl Cutler</li>
      <li>Lena Dale</li><li>Caroline Gable</li><li>Anita Gorman</li><li>Amy Grover</li>
      <li>Clay Hadley</li><li>Mark Hadley</li><li>Molly Hartwell</li><li>Luke Hines</li>
      <li>Mitch Holden</li><li>Nora Hutton</li><li>Tessa Hyde</li><li>Diana Jarvis</li>
      <li>Alice Lowry</li><li>Marla Moffat</li><li>Glen Northcott</li><li>Dean Pollard</li>
      <li>Jack Pettigrew</li><li>Janet Shelby</li><li>Sean Stanwick</li><li>Susie Somers</li>
      <li>Carla Stanton</li><li>Lydia Mercer</li><li>Joanna Thorne</li><li>Kamila Varga</li>
      <li>Karen Walsh</li><li>Simon Wray</li><li>Edith Yates</li><li>Derek Zeller</li>
    </ul>
  </aside>

  <article class="letter">
    <h1 class="salutation">Dear Mr. Carver,</h1>
    <div class="letter-body">
      <p>Lorem ipsum dolor sit amet, consectetur adipiscing elit. Donec orci purus, luctus vitae dignissim eu, iaculis sed purus. Vivamus faucibus, ipsum nec aliquet viverra, leo mauris condimentum ligula, sit amet sagittis enim ligula quis arcu. Nam egestas tortor id nisi porttitor mattis. In tortor ante, ultricies in suscipit a, tempus non massa. Vivamus et auctor mi. Fusce vel massa nulla. Phasellus nec eros mauris, et scelerisque orci.</p>
      <p>Donec malesuada orci vitae nulla accumsan porta a id massa. Quisque accumsan iaculis magna sit amet fringilla. Maecenas consequat, magna eget tincidunt semper, odio nibh rutrum mi, id feugiat ante nisi eu risus. Vestibulum nunc orci, rhoncus a placerat in, ultricies in mi. Cras mattis varius eros, vel fringilla nisi suscipit eget. Quisque scelerisque sagittis nulla at porttitor.</p>
      <p>Sed id augue vitae urna euismod commodo aliquet a quam. Pellentesque arcu velit, cursus et malesuada ut, consequat et diam. Nullam erat sem, rhoncus id ullamcorper vitae, rhoncus et arcu. In ultricies ultricies nulla, ut rutrum nisi iaculis at. Donec eu magna a metus ornare faucibus. Fusce aliquet faucibus ultricies. Morbi semper, est id tincidunt gravida, sem arcu adipiscing lacus, ac bibendum nulla leo eu purus. Quisque nec diam sed risus consectetur a ccumsan quis quis nibh. Vestibulum id purus lorem.</p>
      <p>It is a long established fact that a reader will be distracted by the readable content of a page when looking at its layout. The point of using Lorem Ipsum is that it has a more-or-less normal distribution of letters, as opposed to using 'Content here, content here', making it look like readable English. Many desktop publishing packages</p>
    </div>
  </article>

  <p class="closing">Sincerely,</p>
  <svg class="signature" role="img" aria-label="Handwritten signature of Owen Marsh" viewBox="0 0 124 56">
    <rect x="0" y="0" width="124" height="56" rx="6" fill="var(--signature)" opacity="0.18"/>
  </svg>
</main>
</body>
</html>
```